FinTech Website + Mobile Design.

We require an new fresh Professional looking upgrade for our company website.

We are Australia's first professional crowd funding platform. Currently listed on the QMB(Meridian Trading Board) and soon to be listed on the KPR(Harbourline Equity Market)

We are looking for a clean simple but professional look with clear focus the two main objectives "Investing" and "Borrowing"

Veltrano is a professional crowdfunding platform focused at servicing SME’s and non-sophisticated Investors.
Our platform lets borrowers access funds of $100,000 to $5 Million form our user base of over 50,000 members. Borrowers choose the rate they are prepared offer Investors and Investors select the opportunities they would like to invest in with average returns of 12%pa*.

Our platform gives Investors and borrows a real alternative to conventional banking. Funding can be done in as little as 45days*.

We need the design to be responsive.

The are some Charts and Statistics that will need graphics producing.

We will require Photoshop files, fonts and assets only. Not HTML or CSS.

Reference sites
https://plovenest.com
https://www.brambleworth.com
https://www.zenquarrow.com
https://au.trelvingsharedesk.com/
Updates

This project has been extended by 5 Days. I look forward to see your designs. Cheers Wendell

Dear Designers, Please don't forget to include a Mobile version of your designs. Thanks Wendell

Hi All Designers, I will be closing this project in two days. Don't miss out. Get your designs in as soon as you can. Cheers Wendell

Target Market(s)

Investors, Estate Digest developers, Small business' Medium business.

Industry/Entity Type

Finance

Number of Pages Required

1 page

Font styles to use
Sans Serif

Requirements
Must have
• Clean Professional design
• Bright and fresh look
• Mobile design/responsive
Nice to have
• Animations

```html
<!DOCTYPE html>
<html lang="en">
<head>
<meta charset="utf-8">
<title>Veltrano — Crowdfunding Platform</title>
<link href="https://fonts.googleapis.com/css2?family=Open+Sans:wght@300;400;600;700;800&display=swap" rel="stylesheet">
<style>
:root{
  --orange:#f7941d;
  --yellow:#f6c400;
  --red:#e0262b;
  --green:#3aaa35;
  --blue:#1a7fc1;
  --teal:#1b9cc9;
  --ink:#222;
  --muted:#777;
  --light:#f2f2f2;
  --line:#ddd;
  --dark:#262626;
}
*{box-sizing:border-box;margin:0;padding:0}
html,body{width:1200px;height:3982px;overflow:hidden}
body{font-family:"Open Sans",Arial,sans-serif;color:var(--ink);background:#fff;position:relative}
section,header,footer{position:relative;width:1200px;overflow:hidden}
.abs{position:absolute}

/* header */
.site-header{height:93px;background:#fff;border-bottom:1px solid #eee}
.brand{left:80px;top:28px;font-size:30px;line-height:36px;font-weight:700;color:var(--ink)}
.main-nav{right:70px;top:30px;display:flex;align-items:center;gap:38px;font-size:15px;font-weight:600}
.main-nav a{color:var(--ink);text-decoration:none}
.main-nav .active{color:var(--red)}
.main-nav .join{background:var(--yellow);padding:8px 14px;font-size:17px}
.main-nav .login{font-weight:400}

/* hero */
.hero{height:492px;background:linear-gradient(180deg,#081a52 0%,#0e2f7a 45%,#1c3a6e 65%,#8a6a3b 82%,#2a1b10 100%)}
.hero-lead{top:148px;width:100%;text-align:center;color:#fff;font-size:17px;line-height:24px}
.hero-lead b{color:var(--yellow);text-decoration:underline;font-size:18px}
.hero-cta{top:208px;width:240px;text-align:center}
.hero-cta .box{border:2px solid #fff;height:56px;line-height:52px;color:#fff;font-size:25px;font-weight:700}
.hero-cta .more{display:inline-block;margin-top:2px;width:150px;height:18px;line-height:18px;font-size:11px;color:#fff}

/* press */
.press{height:85px;background:#e8e8e8;display:flex;justify-content:space-around;align-items:center;padding:0 30px}
.press span{font-size:15px;font-weight:700;color:#333}

/* stats */
.stats{height:273px;text-align:center}
.stats h2{padding-top:40px;font-size:30px;line-height:40px;font-weight:700}
.stats h2 em{font-style:normal;color:var(--red)}
.stat-row{display:flex;justify-content:center;margin-top:42px}
.stat{width:300px;border-right:1px solid var(--line)}
.stat:last-child{border:0}
.stat .num{font-size:42px;color:var(--blue);font-weight:400}
.stat .lbl{font-size:14px;color:var(--muted)}

/* chart */
.chart{height:570px;background:var(--light);text-align:center}
.section-title{font-size:28px;font-weight:600}
.chart .section-title{padding-top:44px}
.chart p{width:860px;margin:14px auto 0;font-size:12.5px;line-height:21px;color:var(--muted)}
.chart-svg{left:140px;top:190px}
.chart-note{top:500px;width:100%;font-size:12px;color:#999}
.chart-note b{color:var(--orange)}
.legend{left:960px;text-align:left}
.legend .pct{font-size:34px;font-weight:300}
.legend .name{font-size:13px;font-weight:700;line-height:16px}
.legend .sub{font-size:12px;color:var(--muted)}

/* projects */
.current{height:611px}
.current .section-title{padding-top:40px;text-align:center}
.carousel-arrow{top:270px;font-size:40px;color:#999;font-weight:300}
.card{top:97px;width:236px;border:1px solid var(--line);background:#fff}
.card-img{height:140px;position:relative}
.card-tag{position:absolute;left:0;top:0;background:#222;color:#fff;font-size:13px;font-weight:700;padding:4px 10px}
.card-share{position:absolute;right:8px;top:5px;display:flex;gap:5px}
.card-share i{width:9px;height:9px;border-radius:50%;background:#fff;display:block}
.card-body{padding:12px 12px 14px}
.amount{display:flex;justify-content:space-between;align-items:center;font-size:15px;font-weight:700;color:var(--green)}
.amount small{font-size:10px;color:#333}
.bar{height:6px;background:#ddd;margin:8px 0 8px 26px;position:relative}
.bar::before{content:"";position:absolute;left:0;top:0;height:6px;width:58%;background:var(--teal)}
.card-title{font-size:13px;line-height:18px;border-top:1px solid #eee;padding:8px 0;border-bottom:1px solid #eee}
.facts{display:grid;grid-template-columns:1fr 1fr;gap:8px 6px;font-size:10.5px;padding:10px 0 12px}
.facts span{display:flex;align-items:center;gap:5px}
.facts i{width:9px;height:9px;border-radius:50%;background:var(--teal);display:block;flex:none}
.btn-fund{display:block;border:2px solid var(--green);text-align:center;font-size:13px;font-weight:700;padding:9px 0;color:var(--ink)}

/* members */
.members{height:358px;background:linear-gradient(90deg,#141414,#2e2e2e 55%,#1a1a1a)}
.ring{left:88px;top:57px}
.ring-text{left:88px;top:152px;width:240px;text-align:center;color:#333}
.ring-text .val{font-size:32px;color:var(--blue)}
.ring-text .val b{color:var(--orange);font-weight:400;font-size:24px}
.ring-text .cap{font-size:12px}
.portrait{left:300px;top:40px;width:250px;height:318px;background:linear-gradient(180deg,#5b5b5b,#333 70%,#222)}
.members h3{left:570px;top:60px;width:560px;text-align:center;font-size:28px;font-weight:300;color:#bbb}
.members h3 em{font-style:normal;color:var(--orange)}
.members .quote{left:580px;top:128px;width:540px;font-size:12.5px;line-height:22px;color:#999}
.members .who{left:580px;top:230px;color:#ddd;font-size:13px;font-weight:700}
.members .role{left:580px;top:252px;color:#888;font-size:11px}
.dots{left:580px;top:280px;display:flex;gap:6px}
.dots i{width:6px;height:6px;background:#666;display:block}
.dots i:first-child{background:var(--orange)}

/* testimonials */
.testimonials{height:354px}
.testimonials .section-title{left:240px;top:48px;font-size:34px;font-weight:400}
.t-box{left:115px;top:125px;width:530px;height:165px;background:var(--teal);color:#fff;text-align:center;padding:32px 50px 0;font-size:13px;line-height:20px}
.t-icon{left:355px;top:100px;width:50px;height:50px;border-radius:50%;background:#fff;color:var(--teal);font-size:36px;font-weight:800;text-align:center;line-height:62px}
.t-box .name{margin-top:12px;font-weight:700}
.t-box .name span{font-weight:400;opacity:.7;font-size:11px;padding-left:6px}
.t-arrow{top:195px;color:#aaa;font-size:22px}
.t-logos{left:745px;top:115px;width:370px;display:grid;grid-template-columns:repeat(3,1fr);row-gap:38px;border-right:3px solid #eee}
.t-logos span{font-size:14px;font-weight:700;color:#333}

/* banner */
.banner{height:292px;background:linear-gradient(180deg,#2a1d14,#4a3018 45%,#1c1410);text-align:center}
.banner .mark{padding-top:66px;font-size:62px;font-weight:300;color:#fff;letter-spacing:2px}
.banner .tag{font-size:17px;color:#fff;margin-top:-6px}
.btn-explore{display:inline-block;margin-top:28px;width:188px;height:44px;line-height:44px;background:#f5f5f5;font-size:16px;font-weight:700;color:#222}

/* events */
.events{height:531px;text-align:center}
.events .section-title{padding-top:46px;font-size:36px;font-weight:400}
.event{top:117px;width:464px;height:268px;border:1px solid var(--line);text-align:left;padding:24px 24px 0}
.event-img{height:170px;position:relative}
.date{position:absolute;left:50%;top:70px;display:flex;transform:translateX(-50%)}
.date div{width:40px;text-align:center;color:#fff;font-size:26px;line-height:34px}
.date div small{display:block;background:#fff;color:#333;font-size:10px;line-height:15px}
.date .o{background:var(--orange)}.date .t{background:var(--teal)}
.event-meta{display:flex;justify-content:space-between;margin-top:12px}
.event-meta h4{font-size:16px;font-weight:700}
.event-meta p{font-size:12px;color:var(--muted)}
.event-meta .loc{display:flex;gap:8px;align-items:center;font-size:13px;font-weight:600}
.event-btns{top:433px;width:100%;display:flex;justify-content:center;gap:16px}
.event-btns span{padding:8px 16px;font-size:13px;font-weight:600;border:1px solid var(--line)}
.event-btns .primary{background:var(--orange);border-color:var(--orange);color:#222}

/* footer */
.site-footer{height:323px;background:var(--dark);color:#999;font-size:11px;line-height:17px}
.col h5{color:#fff;font-size:15px;font-weight:600;padding-bottom:8px;margin-bottom:12px;position:relative}
.col h5::after{content:"";position:absolute;left:0;bottom:0;width:26px;height:2px;background:var(--orange)}
.assoc span{display:block;font-size:17px;font-weight:800;color:#ccc;margin-bottom:16px}
.field{width:240px;height:30px;background:#3a3a3a;border:1px solid #444;padding-left:8px;line-height:28px;color:#777}
.btn-submit{display:inline-block;margin-top:6px;margin-left:160px;background:#111;color:#fff;padding:6px 18px;font-size:12px}
.socials{display:flex;gap:10px}
.socials i{width:28px;height:28px;border-radius:50%;background:#3a3a3a;display:block}
.badge{width:64px;height:26px;background:#e9e9e9;margin-bottom:14px;border-radius:3px}
.badge.blue{background:#2a5fb0;width:40px}
</style>
</head>
<body>

<header class="site-header">
  <div class="brand abs">Veltrano</div>
  <nav class="main-nav abs">
    <a class="active">Home</a><a>Invest</a><a>Get Found</a><a>About Us</a>
    <a class="join">Join</a><a class="login">⇥ Login</a>
  </nav>
</header>

<section class="hero" role="img" aria-label="Night skyline of a harbour city with lit towers reflected on the water">
  <div class="hero-lead abs">Lorem ipsum dolor sit amet, consect<br><b>etuer adipiscing elit.</b></div>
  <div class="hero-cta abs" style="left:358px"><div class="box">Invest</div><span class="more" style="background:var(--yellow);color:#222">Learn More</span></div>
  <div class="hero-cta abs" style="left:605px"><div class="box">Get Found</div><span class="more" style="background:var(--red)">Learn More</span></div>
</section>

<section class="press">
  <span>KTV Wire</span><span>Marlo News</span><span>Bay Ledger</span><span>Trade Weekly</span><span>Orbit News</span><span>Coastal Herald</span><span>Pulse Daily</span><span>Tern Report</span><span>Evening Courier</span>
</section>

<section class="stats">
  <h2>Since 2013 we've connected borrowers and investors<br>for loans totalling <em>over $50 million</em></h2>
  <div class="stat-row">
    <div class="stat"><div class="num">70+</div><div class="lbl">Projects funded</div></div>
    <div class="stat"><div class="num">52,000+</div><div class="lbl">User base</div></div>
    <div class="stat"><div class="num">14.5%</div><div class="lbl">Average returns</div></div>
  </div>
</section>

<section class="chart">
  <h2 class="section-title">Return Comparison Chart</h2>
  <p>Historically, investors with roughly 20% allocated to real estate have outperformed those who only own stocks and bonds. However, the best opportunities require minimums of $100,000 or more, making them inaccessible unless you're very wealthy. The only other option is to go through unnecessary middlemen who charge high fees, negatively impacting returns.</p>
  <svg class="chart-svg abs" width="800" height="310" viewBox="0 0 800 310">
    <g stroke="#e2e2e2" stroke-width="1">
      <line x1="40" y1="0" x2="40" y2="270"/><line x1="240" y1="0" x2="240" y2="270"/><line x1="440" y1="0" x2="440" y2="270"/><line x1="640" y1="0" x2="640" y2="270"/>
      <line x1="0" y1="270" x2="800" y2="270" stroke="#ccc"/>
    </g>
    <polyline fill="none" stroke="#cfcfcf" stroke-width="2" points="0,262 100,258 200,255 300,250 400,256 500,248 600,245 700,240 790,236"/>
    <polyline fill="none" stroke="#f7941d" stroke-width="2.5" points="0,262 40,254 80,240 120,232 160,226 200,212 240,205 280,198 320,178 360,170 400,232 440,190 480,170 520,166 560,156 600,134 640,108 680,100 720,66 760,48 790,46"/>
    <g fill="#f7941d">
      <circle cx="40" cy="254" r="5"/><circle cx="80" cy="240" r="5"/><circle cx="120" cy="232" r="5"/><circle cx="160" cy="226" r="5"/><circle cx="200" cy="212" r="5"/><circle cx="240" cy="205" r="5"/><circle cx="280" cy="198" r="5"/><circle cx="320" cy="178" r="5"/><circle cx="360" cy="170" r="5"/><circle cx="400" cy="232" r="5"/><circle cx="440" cy="190" r="5"/><circle cx="480" cy="170" r="5"/><circle cx="520" cy="166" r="5"/><circle cx="560" cy="156" r="5"/><circle cx="600" cy="134" r="5"/><circle cx="640" cy="108" r="5"/><circle cx="680" cy="100" r="5"/><circle cx="720" cy="66" r="5"/><circle cx="760" cy="48" r="5"/><circle cx="790" cy="46" r="5"/>
    </g>
    <g font-family="Open Sans, sans-serif" font-size="13" font-weight="600" fill="#333" text-anchor="middle">
      <text x="20" y="294">2001</text><text x="240" y="294">2006</text><text x="520" y="294">2011</text><text x="770" y="294">2016</text>
    </g>
  </svg>
  <div class="legend abs" style="top:210px"><div class="pct" style="color:var(--orange)">482%</div><div class="name">Real Estate</div><div class="sub">Growth</div></div>
  <div class="legend abs" style="top:340px"><div class="pct" style="color:#999">80%</div><div class="name">Share Index</div><div class="sub">Growth</div></div>
  <div class="chart-note abs">Based on a $10,000 investment in <u>2001</u> <b>▾</b></div>
</section>

<section class="current">
  <h2 class="section-title">Current Project</h2>
  <span class="carousel-arrow abs" style="left:36px">‹</span>
  <span class="carousel-arrow abs" style="left:1146px">›</span>

  <article class="card abs" style="left:90px">
    <div class="card-img" role="img" aria-label="Hand holding a smartphone on a red backdrop" style="background:linear-gradient(135deg,#c4141a,#7a0d10)"><span class="card-tag">Featured!</span><span class="card-share"><i></i><i></i><i></i></span></div>
    <div class="card-body">
      <div class="amount">Aus $3,821,067 <small>58%</small></div><div class="bar"></div>
      <div class="card-title">Merchandisign made easy for the Creators of this World!</div>
      <div class="facts"><span><i></i>12% PA</span><span><i></i>12 Months</span><span><i></i>AU$2,500,000</span><span><i></i>Perth, Australia</span><span><i></i>AU$30,000 min</span><span><i></i>100</span><span><i></i>27 Days Left</span><span><i></i>22 Investors</span></div>
      <a class="btn-fund">Fund this Project</a>
    </div>
  </article>
  <article class="card abs" style="left:350px">
    <div class="card-img" role="img" aria-label="Bottle held up against a bright red backdrop" style="background:linear-gradient(135deg,#d8242b,#5a1c1c)"><span class="card-tag">Featured!</span><span class="card-share"><i></i><i></i><i></i></span></div>
    <div class="card-body">
      <div class="amount">Aus $3,821,067 <small>58%</small></div><div class="bar"></div>
      <div class="card-title">Merchandisign made easy for the Creators of this World!</div>
      <div class="facts"><span><i></i>12% PA</span><span><i></i>12 Months</span><span><i></i>AU$2,500,000</span><span><i></i>Perth, Australia</span><span><i></i>AU$30,000 min</span><span><i></i>100</span><span><i></i>27 Days Left</span><span><i></i>22 Investors</span></div>
      <a class="btn-fund">Fund this Project</a>
    </div>
  </article>
  <article class="card abs" style="left:610px">
    <div class="card-img" role="img" aria-label="Wall of framed photographs in a studio" style="background:linear-gradient(135deg,#8a8a8a,#3a3a3a)"><span class="card-tag">Featured!</span><span class="card-share"><i></i><i></i><i></i></span></div>
    <div class="card-body">
      <div class="amount">Aus $3,821,067 <small>58%</small></div><div class="bar"></div>
      <div class="card-title">Merchandisign made easy for the Creators of this World!</div>
      <div class="facts"><span><i></i>12% PA</span><span><i></i>12 Months</span><span><i></i>AU$2,500,000</span><span><i></i>Perth, Australia</span><span><i></i>AU$30,000 min</span><span><i></i>100</span><span><i></i>27 Days Left</span><span><i></i>22 Investors</span></div>
      <a class="btn-fund">Fund this Project</a>
    </div>
  </article>
  <article class="card abs" style="left:870px">
    <div class="card-img" role="img" aria-label="Two people in printed t-shirts on a dark stage" style="background:linear-gradient(135deg,#3c3c3c,#111)"><span class="card-tag">Featured!</span><span class="card-share"><i></i><i></i><i></i></span></div>
    <div class="card-body">
      <div class="amount">Aus $3,821,067 <small>58%</small></div><div class="bar"></div>
      <div class="card-title">Merchandisign made easy for the Creators of this World!</div>
      <div class="facts"><span><i></i>12% PA</span><span><i></i>12 Months</span><span><i></i>AU$2,500,000</span><span><i></i>Perth, Australia</span><span><i></i>AU$30,000 min</span><span><i></i>100</span><span><i></i>27 Days Left</span><span><i></i>22 Investors</span></div>
      <a class="btn-fund">Fund this Project</a>
    </div>
  </article>
</section>

<section class="members">
  <svg class="ring abs" width="240" height="240" viewBox="0 0 240 240">
    <circle cx="120" cy="120" r="108" fill="#fff"/>
    <circle cx="120" cy="120" r="112" fill="none" stroke="#1b9cc9" stroke-width="10" stroke-dasharray="470 234" transform="rotate(-90 120 120)"/>
    <circle cx="120" cy="120" r="112" fill="none" stroke="#f7941d" stroke-width="10" stroke-dasharray="0 480 180 44" transform="rotate(-90 120 120)"/>
  </svg>
  <div class="ring-text abs"><div class="val"><b>$</b> 248,594</div><div class="cap">invested on the Veltrano</div></div>
  <div class="portrait abs" role="img" aria-label="Portrait of a smiling manager in a dark suit"></div>
  <h3 class="abs">Join <em>107,819</em> other members like you</h3>
  <p class="quote abs">Lorem ipsum dolor sit amet, consectetuer adipiscing elit. Aenean commodo ligula eget dolor. Aenean massa. Cum sociis natoque penatibus et magnis dis parturient montes, nascetur ridiculus mus. Donec quam felis, ultricies nec, pellentesque eu, pretium quis, sem.</p>
  <div class="who abs">Dorian Calloway</div>
  <div class="role abs">Manager</div>
  <div class="dots abs"><i></i><i></i><i></i><i></i></div>
</section>

<section class="testimonials">
  <h2 class="section-title abs">Our Testimonials</h2>
  <span class="t-arrow abs" style="left:86px">‹</span>
  <span class="t-arrow abs" style="left:660px">›</span>
  <div class="t-box abs">
    Lorem ipsum dolor sit amet, con sectetuer adipiscing elit. Aenean commodo ligula eget dolor. Aenean massa. Cum sociis natoque penatibus et magnis dis parturient montes, nascetur ridiculus mus.
    <div class="name">Tessa Marlow<span>Founder</span></div>
  </div>
  <div class="t-icon abs">“</div>
  <div class="t-logos abs">
    <span>KTV Wire</span><span>Marlo News</span><span>Bay Ledger</span>
    <span>Trade Weekly</span><span>Pulse Daily</span><span>Tern Report</span>
    <span>Estate Digest</span><span>The Southerner</span><span>Ridge Property</span>
  </div>
</section>

<section class="banner" role="img" aria-label="Dusky harbour crane yard with warm city lights">
  <div class="mark">FUNDMOSAIC</div>
  <div class="tag">Crowdfunding Everything, Everything Crowdfunding</div>
  <span class="btn-explore">Explore</span>
</section>

<section class="events">
  <h2 class="section-title">Our Projects</h2>
  <article class="event abs" style="left:90px">
    <div class="event-img" role="img" aria-label="Speaker presenting at an expo stage" style="background:linear-gradient(135deg,#6d6d6d,#2c2c2c)">
      <div class="date"><div class="o">02<small>Days</small></div><div class="t">10<small>Month</small></div></div>
    </div>
    <div class="event-meta"><div><h4>Accounting Pitfalls</h4><p>Aug 2, 2016</p></div>
      <div class="loc"><svg width="14" height="20" viewBox="0 0 14 20"><path d="M7 0C3 0 0 3 0 7c0 5 7 13 7 13s7-8 7-13c0-4-3-7-7-7z" fill="#f7941d"/><circle cx="7" cy="7" r="2.5" fill="#fff"/></svg>Lorem ipsum dolor sit amet</div></div>
  </article>
  <article class="event abs" style="left:646px">
    <div class="event-img" role="img" aria-label="Laptop and papers on an office desk" style="background:linear-gradient(135deg,#9b9b9b,#4a4a4a)">
      <div class="date"><div class="o">02<small>Days</small></div><div class="t">10<small>Month</small></div></div>
    </div>
    <div class="event-meta"><div><h4>Accounting Pitfalls</h4><p>Aug 2, 2016</p></div>
      <div class="loc"><svg width="14" height="20" viewBox="0 0 14 20"><path d="M7 0C3 0 0 3 0 7c0 5 7 13 7 13s7-8 7-13c0-4-3-7-7-7z" fill="#f7941d"/><circle cx="7" cy="7" r="2.5" fill="#fff"/></svg>Lorem ipsum dolor sit amet</div></div>
  </article>
  <div class="event-btns abs"><span class="primary">Up Coming Events</span><span>View All Events</span></div>
</section>

<footer class="site-footer">
  <div class="col abs assoc" style="left:90px;top:40px"><h5>Associations</h5><span>Kallo</span><span>Vendrix</span><span>Ostrel's</span></div>
  <div class="col abs" style="left:308px;top:40px;width:240px"><h5>About us</h5>Veltrano is the first fully public listed crowd funding site with offices in Singapore, Australia, Malaysia and more.</div>
  <div class="col abs" style="left:308px;top:150px"><h5>Get in touch</h5><div class="field">Email</div><span class="btn-submit">Submit</span></div>
  <div class="col abs" style="left:582px;top:40px"><h5>For investors</h5>Lorem ipsum dolor sit amet<br>Lorem ipsum dolor<br>Lorem ipsum dolor sit<br>Lorem ipsum dolor sit amet</div>
  <div class="col abs" style="left:582px;top:150px"><h5>Connect us</h5><div class="socials"><i></i><i></i><i></i><i></i><i></i><i></i></div></div>
  <div class="col abs" style="left:797px;top:40px"><h5>For companies</h5>Lorem ipsum<br>Lorem ipsum dolor<br>Lorem ipsum dolor sit<br>Lorem ipsum</div>
  <div class="col abs" style="left:990px;top:40px"><h5>Security</h5><div class="badge"></div><div class="badge blue"></div></div>
  <div class="abs" style="left:797px;top:218px;font-size:9px;color:#666">Copyright © 2016 Veltrano. All rights reserved.</div>
</footer>

</body>
</html>
```